Vorna Fleet business card

I am needing a business card that at a glance shows all the services that we provide emphasizing some more than others. We are a Fleet and Compliance management company as well as a software company. We provide outsourced solutions for KPX compliance and HR services via our own software.
In addition, we do
drug testing
GPS
Cameras
Electronic DVIRS
ELD's

Target Market(s)

Transportation company owners

Industry/Entity Type

Transportation supplier

Contact Information for Business Card

the card should inform potential customers what we do

Other font styles liked:
• I have added brand guidelines. See attached

Requirements
Must have
• See description
Should not have
• Colors outside my brand guide. See attached

```html
<!DOCTYPE html>
<html lang="en">
<head>
<meta charset="utf-8">
<title>Vorna Fleet business card</title>
<link href="https://fonts.googleapis.com/css2?family=Roboto:wght@400;500;700;900&display=swap" rel="stylesheet">
<style>
  :root{
    --bg:#2e2e2e;
    --red:#b0141f;
    --red-deep:#8e0f19;
    --red-bright:#d0202a;
    --black:#141414;
    --paper:#f1f1f1;
    --ink:#1c1c1c;
    --white:#ffffff;
  }
  *{margin:0;padding:0;box-sizing:border-box;}
  html,body{width:1200px;height:1138px;overflow:hidden;}
  body{background:var(--bg);font-family:'Roboto',sans-serif;position:relative;}

  .card{position:absolute;width:620px;height:374px;border-radius:16px;overflow:hidden;}

  /* front */
  .card-front{left:274px;top:186px;
    background:linear-gradient(135deg,var(--red-deep) 0%,var(--red) 45%,var(--red-deep) 100%);}
  .card-front .texture{position:absolute;right:0;top:0;width:300px;height:294px;
    background:linear-gradient(135deg,rgba(255,255,255,0) 30%,rgba(255,255,255,.06) 60%,rgba(0,0,0,.08) 100%);}
  .front-brand{position:absolute;left:0;right:0;top:92px;text-align:center;
    font-weight:900;font-size:70px;line-height:1;color:var(--red-bright);letter-spacing:-1px;}
  .front-url{position:absolute;left:0;right:0;top:230px;text-align:center;
    font-size:15px;letter-spacing:7px;color:var(--black);}
  .services-band{position:absolute;left:0;right:0;top:294px;height:61px;background:var(--black);
    text-align:center;padding-top:10px;}
  .services-title{font-weight:700;font-size:15px;color:var(--red-bright);}
  .services-list{font-size:16.5px;color:#e8e8e8;margin-top:4px;}
  .sep{color:var(--red-bright);margin:0 7px;}

  /* back */
  .card-back{left:276px;top:608px;width:618px;background:var(--paper);}
  .holder{position:absolute;left:50px;top:84px;}
  .holder-name{font-weight:700;font-size:28px;color:var(--red);line-height:1;}
  .holder-role{font-size:16px;color:var(--ink);margin-top:4px;}
  .contacts{position:absolute;left:50px;top:162px;list-style:none;}
  .contacts li{display:flex;align-items:center;height:26px;font-size:16.5px;color:var(--ink);}
  .contacts svg{width:16px;height:16px;margin-right:16px;fill:var(--red);}
  .accent{color:var(--red);}
  .back-brand{position:absolute;right:32px;top:96px;font-weight:900;font-size:52px;color:var(--ink);line-height:1;}
  .back-brand-mark{display:inline-block;width:26px;height:26px;background:var(--red);margin-right:10px;vertical-align:middle;}
  .wave{position:absolute;left:0;top:0;width:618px;height:374px;}
  .back-services{position:absolute;right:33px;top:295px;text-align:right;color:var(--white);}
  .back-services .services-title{color:var(--white);font-size:15.5px;}
  .back-services .line{font-size:15.5px;margin-top:7px;}
  .back-services .sep{color:var(--white);margin:0 6px;}
</style>
</head>
<body>

<section class="card card-front">
  <div class="texture"></div>
  <div class="front-brand">Vorna Fleet</div>
  <div class="front-url">www.vornafleet.com</div>
  <div class="services-band">
    <div class="services-title">OUR SERVICES:</div>
    <div class="services-list">Drug Testing<span class="sep">|</span>GPS<span class="sep">|</span>Cameras<span class="sep">|</span>Electronic DVIRS<span class="sep">|</span>ELD's</div>
  </div>
</section>

<section class="card card-back">
  <svg class="wave" viewBox="0 0 618 374" aria-hidden="true">
    <path d="M0 296 C120 350 250 320 380 270 C470 236 560 220 618 232 L618 374 L0 374 Z" fill="var(--red)"/>
    <path d="M0 322 C140 372 260 340 390 282 C480 244 560 236 618 250 L618 258 C560 246 480 256 395 292 C265 350 140 384 0 336 Z" fill="var(--paper)"/>
    <path d="M40 306 C150 336 250 322 340 290 C250 332 150 346 40 306 Z" fill="var(--paper)"/>
  </svg>

  <div class="holder">
    <div class="holder-name">Dale Mercer</div>
    <div class="holder-role">Co-Founder</div>
  </div>

  <ul class="contacts">
    <li><svg viewBox="0 0 16 16"><path d="M2 6c0-2 2-3 6-3s6 1 6 3l-3 1-1-2H6L5 7 2 6zm2 2h8l1 5H3l1-5zm4 1.5a1.5 1.5 0 100 3 1.5 1.5 0 000-3z"/></svg>480-555-0172</li>
    <li><svg viewBox="0 0 16 16"><path d="M8 1a7 7 0 100 14A7 7 0 008 1zm0 1.5c.8 0 1.7 1.6 2 4H6c.3-2.4 1.2-4 2-4zM2.6 7h2.4c0 .7 0 1.3.1 2H2.6a5.6 5.6 0 010-2zm8.4 0h2.4a5.6 5.6 0 010 2H11c.1-.7.1-1.3 0-2zM6 9.5h4c-.3 2.4-1.2 4-2 4s-1.7-1.6-2-4z"/></svg>www.<span class="accent">vornafleet</span>.com</li>
    <li><svg viewBox="0 0 16 16"><path d="M1 3h14v10H1V3zm1.5 1.3L8 9l5.5-4.7V4.3H2.5z"/></svg>dalemercer@vornafleet.com</li>
  </ul>

  <div class="back-brand"><span class="back-brand-mark"></span>Vorna Fleet</div>

  <div class="back-services">
    <div class="services-title">OUR SERVICES:</div>
    <div class="line">Drug Testing<span class="sep">|</span>GPS<span class="sep">|</span>ELD's</div>
    <div class="line">Cameras<span class="sep">|</span>Electronic DVIRS</div>
  </div>
</section>

</body>
</html>
```